Church Bulletin Ad (see attached sample)

Create a New Church Bulletin Ad. I have attached some samples of what we would like to have in the ad. (1) Marrowfield Realty Thorne Logo (2) Headshot (3) Lena Vasko & Greta Vasko, Real Estate Team (4) Phone number (5) Email address (6) St Aldwin Parishioners for over 40 Years. We would like for the ad to be clean and modern. NO OTHER IMAGES besides headshots and Marrowfield Realty Thorne Logo.

Target Market(s)

Church community

Industry/Entity Type

Real Estate

Font styles to use
Sans Serif
Other font styles liked:
• Modern Font

Colors
0054AA
0677BA
7BADD7
CADEEF
E8F1F8

Requirements
Must have
• Marrowfield Realty Thorne Logo; Headshot; Ad size is 4.5"x1.62"

```html
<!DOCTYPE html>
<html lang="en">
<head>
<meta charset="utf-8">
<title>St Aldwin Bulletin Ad – Vasko Real Estate Team</title>
<link rel="stylesheet" href="https://fonts.googleapis.com/css2?family=Montserrat:wght@400;500;600;700;800&family=Michroma&display=swap">
<style>
  :root {
    --page-bg: #eceaf3;
    --blue-light: #2f72cf;
    --blue-mid: #1f55a8;
    --blue-deep: #173a78;
    --navy: #1b3566;
    --gold: #e3b84a;
    --gold-deep: #a9832f;
    --sand: #d8c8ad;
    --sand-light: #ece2d0;
    --white: #ffffff;
    --ink: #25324a;
    --silver-top: #ffffff;
    --silver-bottom: #b9bfc8;
  }
  html, body {
    margin: 0;
    width: 1200px;
    height: 1200px;
    overflow: hidden;
    background: var(--page-bg);
  }
  .canvas {
    position: relative;
    width: 1200px;
    height: 1200px;
  }
  .bulletin-ad {
    position: absolute;
    left: 60px;
    top: 405px;
    width: 1080px;
    height: 389px;
    box-shadow: 0 6px 18px rgba(40, 40, 80, 0.18);
  }
  .bulletin-ad svg { display: block; width: 100%; height: 100%; }
  .headline { font-family: "Montserrat", sans-serif; font-weight: 700; letter-spacing: 1.5px; }
  .team-names { font-family: "Montserrat", sans-serif; font-weight: 600; fill: var(--gold); }
  .team-label { font-family: "Montserrat", sans-serif; font-weight: 500; fill: var(--white); letter-spacing: 0.5px; }
  .parish-line { font-family: "Michroma", sans-serif; fill: var(--navy); }
  .anniversary-number { font-family: "Montserrat", sans-serif; font-weight: 800; font-style: italic; }
  .contact-text { font-family: "Montserrat", sans-serif; font-weight: 400; fill: var(--ink); }
  .brand-name { font-family: "Montserrat", sans-serif; font-weight: 600; fill: var(--white); letter-spacing: 0.5px; }
</style>
</head>
<body>
<main class="canvas">
  <section class="bulletin-ad">
    <svg viewBox="0 0 900 324" xmlns="http://www.w3.org/2000/svg">
      <defs>
        <linearGradient id="skyGradient" x1="0" y1="0" x2="1" y2="0.3">
          <stop offset="0" stop-color="var(--blue-light)"/>
          <stop offset="0.55" stop-color="var(--blue-mid)"/>
          <stop offset="1" stop-color="var(--blue-deep)"/>
        </linearGradient>
        <linearGradient id="silverText" x1="0" y1="0" x2="0" y2="1">
          <stop offset="0" stop-color="var(--silver-top)"/>
          <stop offset="1" stop-color="var(--silver-bottom)"/>
        </linearGradient>
        <linearGradient id="goldText" x1="0" y1="0" x2="0" y2="1">
          <stop offset="0" stop-color="#f3d47c"/>
          <stop offset="0.6" stop-color="var(--gold)"/>
          <stop offset="1" stop-color="var(--gold-deep)"/>
        </linearGradient>
        <linearGradient id="sandBand" x1="0" y1="0" x2="1" y2="0">
          <stop offset="0" stop-color="var(--sand)"/>
          <stop offset="1" stop-color="var(--sand-light)"/>
        </linearGradient>
        <linearGradient id="underline" x1="0" y1="0" x2="1" y2="0">
          <stop offset="0" stop-color="var(--gold)"/>
          <stop offset="1" stop-color="var(--gold)" stop-opacity="0"/>
        </linearGradient>
        <linearGradient id="portraitTone" x1="0" y1="0" x2="0" y2="1">
          <stop offset="0" stop-color="#6b5a52"/>
          <stop offset="1" stop-color="#2a2626"/>
        </linearGradient>
        <linearGradient id="portraitToneLight" x1="0" y1="0" x2="0" y2="1">
          <stop offset="0" stop-color="#d9d4d0"/>
          <stop offset="1" stop-color="#3a3432"/>
        </linearGradient>
      </defs>

      <rect class="sky-panel" x="0" y="0" width="900" height="324" fill="url(#skyGradient)"/>

      <rect class="headshot headshot-lena" x="6" y="32" width="196" height="240" rx="60" fill="url(#portraitTone)" role="img" aria-label="Headshot of Lena Vasko"/>
      <rect class="headshot headshot-greta" x="200" y="24" width="186" height="236" rx="60" fill="url(#portraitToneLight)" role="img" aria-label="Headshot of Greta Vasko"/>

      <polygon class="sand-band" points="0,266 900,178 900,222 0,307" fill="url(#sandBand)"/>
      <polygon class="white-base" points="0,307 900,222 900,324 0,324" fill="var(--white)"/>

      <text class="headline" x="636" y="48" font-size="36" text-anchor="middle" fill="url(#silverText)">ENERGY. EXCELLENCE</text>
      <text class="headline" x="636" y="88" font-size="36" text-anchor="middle" fill="url(#silverText)">EXPERIENCE</text>
      <rect class="headline-rule" x="503" y="97" width="250" height="3" fill="url(#underline)"/>
      <text class="team-names" x="636" y="126" font-size="20" text-anchor="middle">Lena Vasko &amp; Greta Vasko</text>
      <text class="team-label" x="636" y="151" font-size="17" text-anchor="middle">REAL ESTATE TEAM</text>

      <g class="parish-line-group" transform="rotate(-5.5 60 292)">
        <text class="parish-line" x="60" y="292" font-size="22">St Aldwin Parishioners <tspan font-size="19">for over</tspan></text>
      </g>
      <text class="anniversary-number" x="596" y="238" font-size="78" fill="url(#goldText)" transform="rotate(-5.5 596 238)">40</text>
      <text class="parish-line" x="752" y="214" font-size="19" transform="rotate(-5.5 752 214)">years</text>

      <g class="contact-phone">
        <circle cx="497" cy="283" r="7" fill="var(--gold-deep)"/>
        <path d="M494.2 279.5c.4-.4 1-.4 1.3 0l.9 1.1c.3.4.2.9-.1 1.2l-.5.5c.5 1 1.2 1.8 2.2 2.3l.5-.5c.3-.3.8-.4 1.2-.1l1.1.9c.4.3.4.9 0 1.3l-.6.6c-.8.7-4.9-1.2-6.6-5.1-.3-.8-.2-1.5.6-2.2z" fill="var(--white)"/>
        <text class="contact-text" x="512" y="289" font-size="15.5">(206) 555-0148</text>
      </g>
      <g class="contact-email">
        <circle cx="497" cy="305" r="7" fill="var(--gold-deep)"/>
        <rect x="493" y="302" width="8" height="6" fill="none" stroke="var(--white)" stroke-width="1"/>
        <path d="M493 302l4 3 4-3" fill="none" stroke="var(--white)" stroke-width="1"/>
        <text class="contact-text" x="512" y="311" font-size="15.5">VaskoTeam@MarrowfieldRT.com</text>
      </g>

      <g class="brand-block">
        <rect x="800" y="236" width="88" height="78" fill="var(--navy)"/>
        <text class="brand-name" x="844" y="266" font-size="10" text-anchor="middle">MARROWFIELD</text>
        <text class="brand-name" x="844" y="281" font-size="10" text-anchor="middle">REALTY</text>
        <text class="brand-name" x="844" y="296" font-size="10" text-anchor="middle">THORNE</text>
      </g>
    </svg>
  </section>
</main>
</body>
</html>
```